Security and Staff Identity Business Products Brochure is required.

Looking for a brochure that introduces the business, and the general products and categories we sell.

The flyer will be 2 sided A3 in size, which will be folded in half once printed to effectively be 4 printed sides. 420 x 297mm

I have a lumen-crate account - if there is images you would like to use and i like the design i can purchase them.

As the finalised contact details have not yet available, please ensure that the final contact design can be edited for contact details - Phone, address, email etc.

Content is in the attached files. Ideally the front page will have logo, image/s, and our 3x Value pillars "Global Brands", "Local Supply", "Expert Advice".
Inside will have the 4 product lines w/ content and relevant images.

I have attached an similar brochure for the idea - Titles Tavorn Brochure. PLEASE Note i am after a far more sophisticated and professional looking brochure than this.

Target Market(s)

Potential new customers who need to be introduced to who we are and what range of products we supply

Industry/Entity Type

Security

Other font styles liked:
• Calibri

Colors
abd037
ffffff
919191
1b1b1b
474747
9bcb3c

Requirements
Must have
• Must have 4 categories shown on the inside page/s. Printers, Printer Ribbons, Cards & Access, and Accessories.
• Show the supplier logo's we supply.
• Some not necessarily all corresponding images to those categories.
• Text content in the IDbrochure.docx attachment.
• Must be: 2 sided A3 in size, which will be folded in half once printed to effectively be 4 printed sides. 420 x 297mm
• x Value pillars "Global Brands", "Local Supply", "Expert Advice"
• Colours as per business card and logo design attached.
Nice to have
• Nice to have some background images from Lumen Crate or similar. Business people walking through a business environment.
Should not have
• No cartoons

```html
<!DOCTYPE html>
<html lang="en">
<head>
<meta charset="utf-8">
<title>Verity Crew – Security and Identity Solutions Brochure</title>
<link rel="stylesheet" href="https://fonts.googleapis.com/css2?family=Open+Sans:wght@400;600;700;800&display=swap">
<style>
:root{
  --green:#9bcb3c;
  --green-light:#abd037;
  --green-deep:#6fae1f;
  --white:#ffffff;
  --silver:#919191;
  --ink:#1b1b1b;
  --charcoal:#474747;
  --paper-grey:#e6e6e6;
  --backdrop:#eeeeee;
}
*{box-sizing:border-box;margin:0;padding:0}
html,body{width:902px;height:1200px;overflow:hidden}
body{background:var(--backdrop);font-family:"Open Sans",Calibri,Arial,sans-serif;color:var(--charcoal);position:relative}
.spread{position:absolute;left:79px;width:736px;height:521px;transform:scale(.97);transform-origin:0 0;overflow:hidden;background:var(--white)}
.spread--cover{top:89px}
.spread--inside{top:638px}
.spread svg.layer{position:absolute;left:0;top:0;width:736px;height:521px}
.abs{position:absolute}

/* brand lockup */
.brand{position:absolute;display:flex;align-items:center;gap:8px}
.brand__dot{border-radius:50%;background:var(--green);flex:none}
.brand__name{font-weight:600;color:var(--charcoal);line-height:1}
.brand__tag{font-size:11px;color:var(--charcoal);margin-top:4px;line-height:1}
.brand--cover-front{left:424px;top:26px}
.brand--cover-front .brand__dot{width:46px;height:46px}
.brand--cover-front .brand__name{font-size:31px}
.brand--cover-back{left:190px;top:440px;gap:5px}
.brand--cover-back .brand__dot{width:22px;height:22px}
.brand--cover-back .brand__name{font-size:15px}
.brand--cover-back .brand__tag{font-size:6px;margin-top:2px}
.brand--footer{left:510px;top:440px;gap:5px}
.brand--footer .brand__dot{width:18px;height:18px}
.brand--footer .brand__name{font-size:14px;color:#d7d7d7}

/* contact */
.contact{left:33px;top:440px;list-style:none;font-size:6.5px;font-weight:600;color:var(--charcoal)}
.contact li{display:flex;align-items:center;gap:6px;height:11px}
.contact svg{width:7px;height:7px;fill:var(--green-deep)}

/* images */
.photo{position:absolute;background:linear-gradient(160deg,#f7fbfd 0%,#dfe9ee 45%,#b9c7cf 100%)}
.product{position:absolute;border-radius:4px;background:linear-gradient(160deg,#c9c9c9,#5a5a5a)}
.bubble{position:absolute;width:76px;height:76px;border-radius:50%;border:4px solid var(--green);background:radial-gradient(circle at 45% 40%,#ffffff 0%,#d8d8d8 70%,#9a9a9a 100%);box-shadow:0 1px 3px rgba(0,0,0,.35)}
.bubble--sm{width:66px;height:66px}

/* cover headline */
.cover-title{position:absolute;left:368px;width:368px;top:392px;text-align:center;color:var(--white);font-weight:700;font-size:23.5px;line-height:29px;letter-spacing:.2px}
.pillars{position:absolute;left:397px;top:463px;display:flex;gap:0}
.pillar{display:flex;align-items:center;gap:8px;width:110px;color:var(--white);font-weight:600;font-size:13px;line-height:15px}
.pillar svg{width:22px;height:24px;fill:none;stroke:var(--white);stroke-width:2}
.pillar svg .fill{fill:var(--white);stroke:none}

/* inside */
.section-title{position:absolute;font-weight:700;font-size:10.5px;color:var(--ink);letter-spacing:.1px}
.section-title--on-green{color:var(--white)}
.card{position:absolute;background:var(--white);border:3px solid var(--charcoal);border-radius:9px}
.copy{position:absolute;font-size:6.6px;line-height:9px;color:var(--ink);text-align:justify}
.copy p+p{margin-top:6px}
.suppliers{position:absolute;left:14px;bottom:10px;display:flex;gap:22px;align-items:center}
.suppliers span{font-weight:700;font-size:11px;color:#1f4f9c}
.footer-badge{position:absolute;left:387px;top:426px;width:80px;height:80px;border-radius:50%;background:var(--ink);border:6px solid var(--green)}
.footer-ghost{position:absolute;left:636px;top:428px;width:72px;height:72px;border-radius:50%;background:rgba(255,255,255,.06);border:5px solid rgba(255,255,255,.05)}
.footer-web{position:absolute;left:490px;width:170px;top:472px;text-align:center;font-size:8.5px;color:#e2e2e2}
.ghost-seal{position:absolute;left:58px;top:68px;width:250px;height:250px;border-radius:50%;background:rgba(255,255,255,.07)}
</style>
</head>
<body>

<!-- ============ OUTER SPREAD: back cover + front cover ============ -->
<section class="spread spread--cover" aria-label="Brochure outer spread">
  <svg class="layer" viewBox="0 0 736 521" aria-hidden="true">
    <defs>
      <linearGradient id="coverGreen" x1="0" y1="0" x2="1" y2="0">
        <stop offset="0" stop-color="#8ec63f"/><stop offset=".55" stop-color="#a6d13a"/><stop offset="1" stop-color="#6fb423"/>
      </linearGradient>
      <linearGradient id="coverGrey" x1="0" y1="0" x2="0" y2="1">
        <stop offset="0" stop-color="#ffffff"/><stop offset="1" stop-color="#cfcfcf"/>
      </linearGradient>
      <linearGradient id="darkBand" x1="0" y1="0" x2="1" y2="0">
        <stop offset="0" stop-color="#2a2a2a"/><stop offset="1" stop-color="#111"/>
      </linearGradient>
      <linearGradient id="silverBand" x1="0" y1="0" x2="1" y2="0">
        <stop offset="0" stop-color="#9a9a9a"/><stop offset=".5" stop-color="#f4f4f4"/><stop offset="1" stop-color="#a8a8a8"/>
      </linearGradient>
      <linearGradient id="coverDark" x1="0" y1="0" x2="0" y2="1">
        <stop offset="0" stop-color="#3c3c3c"/><stop offset="1" stop-color="#161616"/>
      </linearGradient>
    </defs>
    <rect x="0" y="0" width="368" height="521" fill="url(#coverGrey)"/>
    <path d="M0,0H368V322C250,332 110,305 0,280Z" fill="url(#coverGreen)"/>
    <path d="M0,280C110,305 250,332 368,322L368,338C250,345 110,340 0,352Z" fill="url(#darkBand)"/>
    <path d="M0,352C110,340 250,345 368,338L368,350C250,358 110,360 0,378Z" fill="url(#silverBand)"/>
    <rect x="368" y="0" width="368" height="521" fill="#ffffff"/>
  </svg>

  <div class="ghost-seal" aria-hidden="true"></div>

  <ul class="abs contact">
    <li><svg viewBox="0 0 10 10"><path d="M2 0.5l2 2-1 1.2c.6 1.4 1.6 2.4 3 3l1.2-1 2 2-1.5 1.8C4 9.3.7 6 .2 2z"/></svg>1234567890</li>
    <li><svg viewBox="0 0 10 10"><path d="M5 0a3.5 3.5 0 0 1 3.5 3.5C8.5 6 5 10 5 10S1.5 6 1.5 3.5A3.5 3.5 0 0 1 5 0zm0 2a1.5 1.5 0 1 0 0 3 1.5 1.5 0 0 0 0-3z"/></svg>compnay address</li>
    <li><svg viewBox="0 0 10 10"><path d="M0 2h10v6H0zM0 2l5 3.5L10 2" /></svg>info@veritycrew.com.au</li>
  </ul>

  <div class="brand brand--cover-back">
    <span class="brand__dot"></span>
    <div><div class="brand__name">Verity Crew</div><div class="brand__tag">Keeping your people and business secure</div></div>
  </div>

  <div class="brand brand--cover-front">
    <span class="brand__dot"></span>
    <div><div class="brand__name">Verity Crew</div><div class="brand__tag">Keeping your people and business secure</div></div>
  </div>

  <div class="photo" style="left:383px;top:95px;width:300px;height:245px" role="img" aria-label="Photo: two business people walking and talking through a bright office corridor"></div>

  <svg class="layer" viewBox="0 0 736 521" aria-hidden="true">
    <path d="M368,330C480,362 620,352 736,283L736,345C620,382 480,382 368,360Z" fill="url(#coverGreen)"/>
    <path d="M368,360C480,382 620,382 736,345L736,364C620,396 480,396 368,378Z" fill="url(#silverBand)"/>
    <path d="M368,378C480,396 620,396 736,364L736,521L368,521Z" fill="url(#coverDark)"/>
  </svg>

  <div class="bubble" style="left:643px;top:107px" role="img" aria-label="Photo: desktop ID card printer"></div>
  <div class="bubble" style="left:643px;top:190px" role="img" aria-label="Photo: colour printer ribbon cartridge"></div>
  <div class="bubble" style="left:643px;top:268px" role="img" aria-label="Photo: retractable badge reels"></div>

  <h1 class="cover-title">SECURITY AND IDENTITY<br>SOLUTIONS</h1>

  <div class="pillars">
    <div class="pillar">
      <svg viewBox="0 0 22 24"><path class="fill" d="M11 1a8 8 0 0 1 8 8c0 6-8 14-8 14S3 15 3 9a8 8 0 0 1 8-8zm0 5a3 3 0 1 0 0 6 3 3 0 0 0 0-6z"/></svg>
      <span>Local<br>Supply</span>
    </div>
    <div class="pillar">
      <svg viewBox="0 0 24 24"><circle cx="12" cy="12" r="10"/><ellipse cx="12" cy="12" rx="4.5" ry="10"/><path d="M2 12h20M4 6.5h16M4 17.5h16"/></svg>
      <span>Global<br>Brands</span>
    </div>
    <div class="pillar">
      <svg viewBox="0 0 26 24"><circle class="fill" cx="9" cy="8" r="4.5"/><path class="fill" d="M1 21c0-5 3.5-7.5 8-7.5s8 2.5 8 7.5z"/><circle class="fill" cx="18" cy="7" r="3.5"/><path class="fill" d="M14 13.2c1.2-.6 2.5-.9 4-.9 4 0 7 2.2 7 6.7h-6.5c-.4-2.4-2-4.3-4.5-5.8z"/></svg>
      <span>Expert<br>Advice</span>
    </div>
  </div>
</section>

<!-- ============ INNER SPREAD: product lines ============ -->
<section class="spread spread--inside" aria-label="Brochure inner spread">
  <svg class="layer" viewBox="0 0 736 521" aria-hidden="true">
    <defs>
      <linearGradient id="innerGrey" x1="0" y1="0" x2="0" y2="1">
        <stop offset="0" stop-color="#ffffff"/><stop offset=".6" stop-color="#e3e3e3"/><stop offset="1" stop-color="#c9c9c9"/>
      </linearGradient>
      <linearGradient id="innerGreen" x1="0" y1="0" x2="1" y2="1">
        <stop offset="0" stop-color="#8ec63f"/><stop offset=".5" stop-color="#abd037"/><stop offset="1" stop-color="#74b526"/>
      </linearGradient>
      <linearGradient id="innerSilver" x1="0" y1="0" x2="1" y2="0">
        <stop offset="0" stop-color="#a0a0a0"/><stop offset=".5" stop-color="#f2f2f2"/><stop offset="1" stop-color="#a0a0a0"/>
      </linearGradient>
      <linearGradient id="footerDark" x1="0" y1="0" x2="1" y2="0">
        <stop offset="0" stop-color="#ffffff"/><stop offset=".2" stop-color="#3a3a3a"/><stop offset="1" stop-color="#141414"/>
      </linearGradient>
    </defs>
    <rect x="0" y="0" width="736" height="521" fill="url(#innerGrey)"/>
    <path d="M0,0H368V72C260,38 120,25 0,26Z" fill="#1f1f1f"/>
    <path d="M0,26C120,25 260,38 368,72L368,90C260,55 120,45 0,46Z" fill="url(#innerSilver)"/>
    <path d="M368,0H736V22C620,22 480,38 368,72Z" fill="url(#innerGreen)"/>
    <path d="M368,72C480,38 620,22 736,22L736,38C620,38 480,55 368,90Z" fill="url(#innerSilver)"/>
    <path d="M0,246C120,236 250,236 368,244V500H0Z" fill="url(#innerGreen)"/>
    <rect x="0" y="500" width="368" height="21" fill="#1f1f1f"/>
    <rect x="368" y="432" width="368" height="68" fill="url(#footerDark)"/>
    <rect x="368" y="500" width="368" height="21" fill="url(#innerGreen)"/>
  </svg>

  <!-- ID card printers -->
  <h2 class="section-title" style="left:35px;top:63px">ID CARD PRINTERS</h2>
  <div class="card" style="left:20px;top:88px;width:330px;height:170px">
    <div class="product" style="left:7px;top:8px;width:132px;height:90px" role="img" aria-label="Photo: black and grey desktop card printer"></div>
    <div class="copy" style="left:146px;top:10px;width:170px">Whether you're looking for a plastic card printer for staff ID , membership cards, or secure access control cards we supply some of the world's leading brands of ID card printers. The brands we supply ensure our customers have the best quality solution and most reliable hardware available.</div>
    <div class="copy" style="left:12px;top:103px;width:145px;text-align:left">With ID card systems from Verity Crew you're taking a critical step to a more secure business environment. ID card solutions for all applications and budgets are readily available.</div>
    <div class="product" style="left:160px;top:76px;width:160px;height:84px;background:linear-gradient(160deg,#ffffff,#c8c8c8 55%,#555)" role="img" aria-label="Photo: two white and grey card printers"></div>
  </div>

  <!-- Printer ribbons -->
  <h2 class="section-title section-title--on-green" style="left:35px;top:287px">PRINTER RIBBONS AND MAINTENANCE</h2>
  <div class="card" style="left:20px;top:310px;width:312px;height:180px">
    <div class="product" style="left:10px;top:12px;width:108px;height:58px;background:linear-gradient(90deg,#2f8fd3,#e0218a 40%,#f5e33b 70%,#3c3c3c)" role="img" aria-label="Photo: colour ribbon cartridge"></div>
    <div class="copy" style="left:126px;top:10px;width:134px">We supply card printer ribbons for a range of different model card printers. Whether you're printing single sided, or double sided, colour or monochrome we have the print consumables and recommendations to suit.</div>
    <div class="copy" style="left:10px;top:80px;width:250px;text-align:left"><p>Talk to us today and let us help you out with selecting the right printer ribbons for your printer today.</p><p>Plastic card printers require care and regular maintenance to ensure they operate at peak performance. Our cleaning kits will ensure the upkeep of your printer is an easy process.</p></div>
    <div class="suppliers" aria-label="Supplier brands">
      <span>Cardline</span><span style="color:#d0302b">Pressa</span><span style="color:#1f4f9c">Tarvo</span><span style="color:#1f4f9c">Printwell</span>
    </div>
  </div>
  <div class="bubble bubble--sm" style="left:289px;top:275px" role="img" aria-label="Photo: colour printer ribbon roll"></div>
  <div class="bubble bubble--sm" style="left:289px;top:351px" role="img" aria-label="Photo: printer cleaning roller"></div>
  <div class="bubble bubble--sm" style="left:289px;top:427px" role="img" aria-label="Photo: ribbon cartridge"></div>

  <!-- Cards and access -->
  <h2 class="section-title" style="left:418px;top:79px">CARDS AND ACCESS CONTROL</h2>
  <div class="card" style="left:393px;top:100px;width:327px;height:130px">
    <div class="product" style="left:10px;top:8px;width:140px;height:108px;background:linear-gradient(160deg,#eef3f7,#8a8a8a 55%,#222)" role="img" aria-label="Photo: smartphone, wall card reader, key fob and access card"></div>
    <div class="copy" style="left:160px;top:22px;width:150px"><p>Verity Crew supply genuine Kestrel access control cards, if you're running an existing Proxima, Vantage, Orbis or Lindara access control card solution, why not ask us today for quote.</p><p>Looking for Key fobs or wristbands? We can help you out with the same level of expertise, advice and customer experience we pride ourselves on.</p></div>
  </div>

  <!-- ID accessories -->
  <h2 class="section-title" style="left:418px;top:253px">ID ACCESSORIES</h2>
  <div class="card" style="left:392px;top:275px;width:328px;height:150px">
    <div class="product" style="left:22px;top:6px;width:48px;height:72px;background:linear-gradient(160deg,#555,#1b1b1b)" role="img" aria-label="Photo: rigid card holder"></div>
    <div class="copy" style="left:106px;top:6px;width:205px;text-align:left"><p>Verity Crew provide a wide range of options on card holders, lanyards, retractable card reels, clips and lapels.</p><p>Made from high quality materials and readily available talk to us today and find out what makes us different to your existing supplier.</p><p>We can customise your accessories with corporate logo's and branding on their ID card holders, lanyards and clips and zingers.</p></div>
    <div class="product" style="left:12px;top:84px;width:300px;height:55px;background:linear-gradient(90deg,#c9d3e6,#2d6bb8 30%,#8a8a8a 55%,#e05a6a 75%,#333)" role="img" aria-label="Photo: badge reels, wristbands, key fob, lanyard and yo-yo clip"></div>
  </div>

  <!-- footer -->
  <div class="footer-badge" aria-hidden="true"></div>
  <div class="footer-ghost" aria-hidden="true"></div>
  <div class="brand brand--footer">
    <span class="brand__dot"></span>
    <div class="brand__name">Verity Crew</div>
  </div>
  <div class="footer-web">www.veritycrew.com.au</div>
</section>

</body>
</html>
```